Brightstep Foot Care Advertisement Sandwich board

We need a Sandwich board design for our fungal nail clinic - please find attached the sandwich board dimensions.

The sandwich board itself will be displayed outside of a large health clinic and we need it to attract the attention of people walking by. We need a brochure holder included in the design which will hold our brochures which provides as clients with more information (please see attached also).

We are open to the designers creativity but we would like a similar theme portrayed on our board that is similar to our website (www.brightstepfootcare.co.nz) and brochure that incorporates our logo which I have attached). The final design should communicate professionalism and be a minimalist look but modern to capture the attention of pedestrians.

Finally, we would like the website and phone number (07) 312 5840.

We look forward to seeing your work.

```html
<!DOCTYPE html>
<html lang="en">
<head>
<meta charset="utf-8">
<title>Brightstep Foot Care – Sandwich Board</title>
<link rel="stylesheet" href="https://fonts.googleapis.com/css2?family=Noto+Serif:wght@400;700&family=Montserrat:wght@400;700&display=swap">
<style>
  :root {
    --backdrop: #d6fcf7;
    --brand-blue: #4663ad;
    --ink-navy: #1f2f7a;
    --accent-grey: #a3a3a3;
    --paper: #ffffff;
    --photo-light: #f6f7f5;
    --photo-skin: #ecd3c3;
  }
  html, body {
    margin: 0;
    padding: 0;
    width: 767px;
    height: 1200px;
    overflow: hidden;
    background: var(--backdrop);
  }
  .board {
    position: absolute;
    left: 33px;
    top: 156px;
    width: 700px;
    height: 887px;
    overflow: hidden;
    background: var(--paper);
    box-shadow: 0 18px 30px rgba(40, 90, 85, 0.35);
    font-family: "Noto Serif", Georgia, serif;
    color: var(--paper);
  }
  .board-photo {
    position: absolute;
    left: 300px;
    top: 0;
    width: 400px;
    height: 887px;
    background: linear-gradient(160deg, var(--photo-light) 0%, var(--photo-skin) 45%, var(--photo-light) 90%);
  }
  .board-shape {
    position: absolute;
    inset: 0;
  }
  .brand {
    position: absolute;
    left: 0;
    width: 324px;
    top: 24px;
    text-align: center;
  }
  .brand-mark {
    display: block;
    width: 70px;
    height: 70px;
    margin: 0 auto 14px;
    border-radius: 50%;
    background: var(--paper);
  }
  .brand-name {
    font-size: 20px;
    letter-spacing: 2px;
    white-space: nowrap;
  }
  .headline {
    position: absolute;
    left: 0;
    width: 296px;
    top: 196px;
    margin: 0;
    text-align: center;
    font-weight: 400;
    font-size: 60px;
    line-height: 58px;
  }
  .treatments-tag {
    position: absolute;
    left: 22px;
    top: 466px;
    width: 253px;
    height: 36px;
    border: 2px solid var(--ink-navy);
    border-radius: 20px;
    background: var(--paper);
    color: var(--ink-navy);
    font-weight: 700;
    font-size: 23px;
    line-height: 36px;
    text-align: center;
  }
  .treatment-list {
    position: absolute;
    left: 36px;
    top: 534px;
    margin: 0;
    padding: 0;
    list-style: none;
  }
  .treatment-list li {
    display: flex;
    align-items: center;
    height: 39.5px;
    font-size: 29px;
  }
  .treatment-dot {
    width: 27px;
    height: 27px;
    margin-right: 15px;
    border-radius: 50%;
    background: var(--paper);
  }
  .contact-phone {
    position: absolute;
    left: 34px;
    top: 758px;
    display: flex;
    align-items: center;
    font-weight: 700;
    font-size: 46px;
    line-height: 56px;
    white-space: nowrap;
  }
  .contact-phone svg { margin-right: 10px; }
  .contact-web {
    position: absolute;
    left: 36px;
    top: 816px;
    display: flex;
    align-items: center;
    font-family: "Montserrat", Arial, sans-serif;
    font-size: 17px;
    white-space: nowrap;
  }
  .contact-web svg { margin-right: 28px; }
  .contact-web strong { font-weight: 700; }
</style>
</head>
<body>
  <main class="board">
    <div class="board-photo" role="img" aria-label="Photograph of smooth bare legs and feet on tiptoe, a hand resting on the knee, against a white background"></div>

    <svg class="board-shape" width="700" height="887" viewBox="0 0 700 887" aria-hidden="true">
      <path fill="var(--accent-grey)" transform="translate(26 0)" d="M0,0 H410 C320,120 290,320 340,460 C380,560 470,620 460,724 C455,800 430,850 414,887 H0Z"/>
      <path fill="var(--paper)" transform="translate(12 0)" d="M0,0 H410 C320,120 290,320 340,460 C380,560 470,620 460,724 C455,800 430,850 414,887 H0Z"/>
      <path fill="var(--brand-blue)" d="M0,0 H410 C320,120 290,320 340,460 C380,560 470,620 460,724 C455,800 430,850 414,887 H0Z"/>
    </svg>

    <header class="brand">
      <span class="brand-mark"></span>
      <div class="brand-name">BRIGHTSTEP FOOT CARE</div>
    </header>

    <h1 class="headline">Your<br>Fungal<br>Nail<br>Experts</h1>

    <div class="treatments-tag">Treatments offered</div>

    <ul class="treatment-list">
      <li><span class="treatment-dot"></span>Cold Laser</li>
      <li><span class="treatment-dot"></span>Topical</li>
      <li><span class="treatment-dot"></span>Oral</li>
      <li><span class="treatment-dot"></span>Surgery</li>
      <li><span class="treatment-dot"></span>General Nail Care</li>
    </ul>

    <div class="contact-phone">
      <svg width="34" height="34" viewBox="0 0 24 24" aria-hidden="true">
        <path fill="var(--paper)" d="M6.6 10.8a15.1 15.1 0 0 0 6.6 6.6l2.2-2.2a1 1 0 0 1 1-.25 11.4 11.4 0 0 0 3.6.57 1 1 0 0 1 1 1V20a1 1 0 0 1-1 1A17 17 0 0 1 3 4a1 1 0 0 1 1-1h3.5a1 1 0 0 1 1 1c0 1.25.2 2.45.57 3.57a1 1 0 0 1-.25 1z"/>
        <path fill="none" stroke="var(--paper)" stroke-width="1.8" stroke-linecap="round" d="M14.5 3.5a6 6 0 0 1 6 6M14.5 7a2.6 2.6 0 0 1 2.5 2.5"/>
      </svg>
      (07) 312 5840
    </div>

    <div class="contact-web">
      <svg width="20" height="20" viewBox="0 0 20 20" aria-hidden="true">
        <g fill="none" stroke="var(--paper)" stroke-width="1.2">
          <circle cx="10" cy="10" r="8.5"/>
          <ellipse cx="10" cy="10" rx="3.8" ry="8.5"/>
          <path d="M1.5 10h17M3 5.5h14M3 14.5h14"/>
        </g>
      </svg>
      <span>www.<strong>brightstepfootcare</strong>.co.nz</span>
    </div>
  </main>
</body>
</html>
```